Makeup Artist looking to redesign business card

I'm a makeup artist relocating from Sydney to the Tweed Heads Area. I will be providing makeup services (primarily in bridal/wedding, events) in the Tweed Heads, Gold Coast and Byron Bay areas. I have attached 2 photos to use on the front OR back of the card. I can't decide which photo will work best, so I have provided both for you to decide. I'm open to the idea of a logo creation, or just the business name. Business name is;
Marlena Ruth Copley Makeup Artist
or
Marlena Copley Makeup Artist
I will need a space for ABN, mobile number, email address and website address.
I'm open to the photo being either colour or B&W.
Font and background colour could be B&W or another colour, again I'm looking for something different and creative, which is why I'm posting this ad.
I do like the idea of the photo being panoramic, so the veil material continues off to the side.
I'm excited to see what people come up with!!!
Target Market(s)
ladies
Industry/Entity Type
Business
Contact Information for Business Card
or

```html
<!DOCTYPE html>
<html lang="en">
<head>
<meta charset="utf-8">
<title>Marlena Ruth Copley Makeup Artist – Business Card</title>
<link href="https://fonts.googleapis.com/css2?family=Questrial&display=swap" rel="stylesheet">
<style>
  :root {
    --canvas: #e8e5e0;
    --card-black: #050505;
    --ink-white: #f2f2f2;
    --ornament-grey: #d9d9d9;
    --photo-light: #f4f3f2;
    --photo-mid: #e6e2df;
    --photo-warm: #d9b9a6;
    --shadow: rgba(0, 0, 0, 0.25);
  }
  * { box-sizing: border-box; margin: 0; padding: 0; }
  html, body {
    width: 1200px;
    height: 780px;
    overflow: hidden;
    background: var(--canvas);
    font-family: "Questrial", "Century Gothic", sans-serif;
  }
  .sheet {
    width: 1200px;
    height: 780px;
    display: flex;
    align-items: center;
    justify-content: center;
    gap: 40px;
  }
  .card {
    position: relative;
    width: 540px;
    height: 309px;
    background: var(--card-black);
    overflow: hidden;
    box-shadow: 0 10px 28px var(--shadow);
  }

  /* Front: portrait panel + contact details */
  .portrait-panel {
    position: absolute;
    inset: 0;
  }
  .portrait-panel svg { display: block; }

  .front-identity {
    position: absolute;
    top: 34px;
    left: 300px;
    width: 210px;
    text-align: center;
    color: var(--ink-white);
  }
  .contact-list {
    position: absolute;
    left: 300px;
    top: 168px;
    width: 210px;
    list-style: none;
    color: var(--ink-white);
    font-size: 13.5px;
    line-height: 1.75;
    letter-spacing: 0.2px;
  }

  /* Back: centred identity */
  .back-identity {
    position: absolute;
    inset: 0;
    display: flex;
    flex-direction: column;
    align-items: center;
    justify-content: center;
    color: var(--ink-white);
    text-align: center;
  }

  .ornament {
    display: block;
    margin: 0 auto;
    background: var(--ornament-grey);
    border-radius: 3px;
  }
  .ornament--top { width: 120px; height: 20px; margin-bottom: 8px; }
  .ornament--bottom { width: 120px; height: 20px; margin-top: 8px; }
  .back-identity .ornament--top,
  .back-identity .ornament--bottom { width: 150px; height: 26px; }

  .business-name {
    font-size: 17px;
    line-height: 1.2;
    font-weight: 400;
    letter-spacing: 0.3px;
  }
  .back-identity .business-name { font-size: 22px; }
</style>
</head>
<body>
  <main class="sheet">

    <section class="card card--front" aria-label="Business card front">
      <div class="portrait-panel">
        <svg width="540" height="309" viewBox="0 0 540 309">
          <defs>
            <linearGradient id="portraitTone" x1="0" y1="0" x2="1" y2="1">
              <stop offset="0" stop-color="var(--photo-light)"/>
              <stop offset="0.45" stop-color="var(--photo-warm)" stop-opacity="0.55"/>
              <stop offset="1" stop-color="var(--photo-mid)"/>
            </linearGradient>
          </defs>
          <path class="portrait-area" role="img"
                aria-label="Portrait photograph of the makeup artist in a soft white veil"
                d="M0 0 H150 C215 0 215 95 255 190 C280 255 275 290 290 309 H0 Z"
                fill="url(#portraitTone)"/>
          <path class="wave-edge" d="M150 0 C215 0 215 95 255 190 C280 255 275 290 290 309"
                fill="none" stroke="#bdbdbd" stroke-width="3"/>
        </svg>
      </div>

      <div class="front-identity">
        <span class="ornament ornament--top" role="img" aria-label="Scroll ornament"></span>
        <h1 class="business-name">Marlena Ruth Copley<br>Makeup Artist</h1>
        <span class="ornament ornament--bottom" role="img" aria-label="Scroll ornament"></span>
      </div>

      <ul class="contact-list">
        <li class="contact-phone">0412 738 560</li>
        <li class="contact-email">hello@copleymakeup.com.au</li>
        <li class="contact-web">www.copleymakeup.com.au</li>
        <li class="contact-abn">ABN: 51824753556</li>
      </ul>
    </section>

    <section class="card card--back" aria-label="Business card back">
      <div class="back-identity">
        <span class="ornament ornament--top" role="img" aria-label="Scroll ornament"></span>
        <h2 class="business-name">Marlena Ruth Copley<br>Makeup Artist</h2>
        <span class="ornament ornament--bottom" role="img" aria-label="Scroll ornament"></span>
      </div>
    </section>

  </main>
</body>
</html>
```